Business card design for online Mandarin Learning School

We need a business card design for our online language learning school called "Sunny Kite Academy for Mandarin Learning". Our existing website is https://www.sunnykiteacademy.com
We have our logo already. We would like to see our business card design that can make our online teaching services to be innovative, young, energetic and fun to learn. Prefer to have a certain level of color matching with our website. Apart from "Sunny Kite Academy", need to specifically state "for Mandarin Learning" as well on the business card.

```html
<!DOCTYPE html>
<html lang="en">
<head>
<meta charset="utf-8">
<title>Sunny Kite Academy – Business Card</title>
<link href="https://fonts.googleapis.com/css2?family=Lato:wght@400;700&display=swap" rel="stylesheet">
<style>
  :root {
    --teal: #2bb1bd;
    --teal-dark: #1f9aa6;
    --coral: #e2605d;
    --white: #ffffff;
    --ink-grey: #6d6e71;
    --backdrop: #e9eaec;
  }
  * { box-sizing: border-box; margin: 0; padding: 0; }
  html, body { width: 1200px; height: 715px; overflow: hidden; }
  body {
    background: var(--backdrop);
    font-family: "Lato", Arial, sans-serif;
    display: flex;
    align-items: center;
    justify-content: center;
    gap: 50px;
  }
  .card {
    position: relative;
    width: 525px;
    height: 300px;
    overflow: hidden;
    box-shadow: 0 6px 18px rgba(0,0,0,0.18);
  }
  .card-front {
    background: var(--teal);
    display: flex;
    align-items: center;
    justify-content: center;
  }
  .brand {
    display: flex;
    align-items: center;
    gap: 12px;
  }
  .brand-dot {
    width: 14px; height: 14px;
    border-radius: 50%;
    background: var(--white);
  }
  .brand-name {
    font-family: "Lato", Arial, sans-serif;
    font-weight: 400;
    font-size: 30px;
    letter-spacing: 2px;
    text-transform: uppercase;
    color: var(--white);
    line-height: 1.15;
  }
  .card-front .brand-name small,
  .card-back .brand-name small { display: block; font-size: 13px; letter-spacing: 2.5px; }

  .card-back { background: var(--teal); }
  .card-back .shape { position: absolute; inset: 0; }
  .contact {
    position: absolute;
    left: 30px;
    top: 40px;
    color: var(--white);
  }
  .person-name {
    font-weight: 700;
    font-size: 20px;
    letter-spacing: 1px;
    text-transform: uppercase;
  }
  .person-role { font-size: 12px; margin-bottom: 22px; }
  .address { font-size: 13px; line-height: 1.35; margin-bottom: 14px; }
  .contact-list { list-style: none; font-size: 13px; line-height: 1.5; }
  .contact-list li { display: flex; align-items: center; gap: 8px; }
  .contact-list svg { width: 10px; height: 10px; flex: none; }
  .card-back .brand {
    position: absolute;
    left: 335px;
    top: 125px;
    width: 175px;
    gap: 8px;
  }
  .card-back .brand-dot { background: var(--coral); width: 10px; height: 10px; }
  .card-back .brand-name { color: var(--teal-dark); font-size: 19px; letter-spacing: 1.5px; }
  .card-back .brand-name small { font-size: 9px; letter-spacing: 1.5px; }
</style>
</head>
<body>
  <section class="card card-front">
    <div class="brand">
      <span class="brand-dot"></span>
      <div class="brand-name">Sunny Kite Academy<small>for Mandarin Learning</small></div>
    </div>
  </section>

  <section class="card card-back">
    <svg class="shape" viewBox="0 0 525 300" aria-hidden="true">
      <circle cx="455" cy="195" r="178" fill="var(--coral)"/>
      <circle cx="462" cy="195" r="174" fill="var(--white)"/>
    </svg>
    <div class="contact">
      <div class="person-name">Daniela Moreau</div>
      <div class="person-role">Director</div>
      <div class="address">2870 Larkspur Lane<br>Halden, MT 59102</div>
      <ul class="contact-list">
        <li><svg viewBox="0 0 10 10"><path d="M2 0.5 L3.8 2.5 L2.8 3.6 Q4 6 6.4 7.2 L7.5 6.2 L9.5 8 L8.3 9.5 Q1 8 0.5 1.7 Z" fill="currentColor"/></svg>+330 2715-4639</li>
        <li><svg viewBox="0 0 10 10"><rect x="0.5" y="2" width="9" height="6" fill="none" stroke="currentColor"/><path d="M0.5 2 L5 5.5 L9.5 2" fill="none" stroke="currentColor"/></svg>info@sunnykiteacademy.com</li>
        <li><svg viewBox="0 0 10 10"><circle cx="5" cy="5" r="4.3" fill="none" stroke="currentColor"/><ellipse cx="5" cy="5" rx="1.8" ry="4.3" fill="none" stroke="currentColor"/><path d="M0.7 5 H9.3" stroke="currentColor"/></svg>www.sunnykiteacademy.com</li>
      </ul>
    </div>
    <div class="brand">
      <span class="brand-dot"></span>
      <div class="brand-name">Sunny Kite Academy<small>for Mandarin Learning</small></div>
    </div>
  </section>
</body>
</html>
```